LLC needs a business card design that emphasizes consulting and expert witness in upstream oil and g

I need a business card design for my company called Velmo Consultative Service, LLC. My expertise is in oil and gas upstream operations management to optimize performance and also as an expert witness for law firms in oil and gas upstream operations litigation.
The final design should communicate knowledge and hands-on experience as well as trust. (Velmo means rope or lasso. Perhaps "Velmo" should be in the form of a rope.) I do not like the color green in any shade. My first preference would be some shade of blue.

```html
<!DOCTYPE html>
<html lang="en">
<head>
<meta charset="utf-8">
<title>Velmo Consultative Service, LLC — Business Card</title>
<link href="https://fonts.googleapis.com/css2?family=Arimo:wght@400;700&display=swap" rel="stylesheet">
<style>
  :root {
    --navy: #1f3f7a;
    --navy-light: #2c4d8c;
    --paper: #ffffff;
    --paper-soft: #f1f1f1;
    --stage: #e6e4e0;
    --ink-on-navy: #ffffff;
    --brand: #1f3f7a;
    --rule: #c9d3e6;
  }
  * { box-sizing: border-box; margin: 0; padding: 0; }
  html, body {
    width: 1200px; height: 892px; overflow: hidden;
    background: var(--stage);
    font-family: "Arimo", Arial, sans-serif;
  }
  .canvas { position: relative; width: 1200px; height: 892px; }
  .card {
    position: absolute; width: 540px; height: 308px;
    overflow: hidden; box-shadow: 0 6px 18px rgba(0,0,0,.18);
  }
  .card--back { left: 600px; top: 90px; background: var(--paper-soft); }
  .card--front { left: 60px; top: 494px; background: var(--paper); }

  .band { position: absolute; left: 0; right: 0; background: linear-gradient(120deg, var(--navy), var(--navy-light)); }
  .card--back .band { top: 0; height: 118px; }
  .card--front .band { top: 138px; bottom: 0; }

  .brand {
    position: absolute; display: flex; align-items: center; gap: 10px;
    color: var(--brand); font-weight: 700; font-size: 25px; letter-spacing: .2px; white-space: nowrap;
  }
  .brand__dot { width: 12px; height: 12px; border-radius: 50%; background: var(--brand); flex: none; }
  .card--back .brand { left: 60px; top: 196px; }
  .card--front .brand { left: 44px; top: 58px; }

  .person { position: absolute; left: 40px; top: 154px; color: var(--ink-on-navy); }
  .person__name { font-size: 24px; font-weight: 400; }
  .person__title { font-size: 11px; margin-top: 3px; }

  .rule { position: absolute; left: 250px; right: 30px; top: 204px; height: 1px; background: var(--rule); }

  .contact {
    position: absolute; left: 250px; top: 214px; color: var(--ink-on-navy);
    font-size: 12.5px; line-height: 1.35; list-style: none;
  }
</style>
</head>
<body>
<main class="canvas">
  <section class="card card--back" aria-label="Card back">
    <div class="band"></div>
    <div class="brand"><span class="brand__dot"></span>Velmo Consultative Service, LLC</div>
  </section>

  <section class="card card--front" aria-label="Card front">
    <div class="brand"><span class="brand__dot"></span>Velmo Consultative Service, LLC</div>
    <div class="band"></div>
    <div class="person">
      <p class="person__name">Employee name</p>
      <p class="person__title">Managing Director</p>
    </div>
    <div class="rule"></div>
    <ul class="contact">
      <li>036-7190 2284</li>
      <li>Info@youremail.com</li>
      <li>www.yourwebsit.com</li>
      <li>Your Address Inc 2nd Lane Ave Linford,</li>
      <li>NJ&nbsp; 00000</li>
    </ul>
  </section>
</main>
</body>
</html>
```